Realty Group Needs Classy, Contemporary Letterhead Design

We need a letterhead design for a new realty company located in NY, USA. We buy investment properties to rehabilitate and or keep in our rental portfolio.

```html
<!DOCTYPE html>
<html lang="en">
<head>
<meta charset="utf-8">
<title>Meridian Realty Group – Letterhead</title>
<link rel="stylesheet" href="https://fonts.googleapis.com/css2?family=Carlito:wght@400&family=Montserrat:wght@400;500;700;800&display=swap">
<style>
  :root {
    --brand-purple: #4a2a86;
    --ink: #3d3d3d;
    --ink-dark: #1e1e1e;
    --paper: #ffffff;
    --backdrop: #e2e2e2;
    --signature-tone: #ececec;
  }
  * { margin: 0; padding: 0; box-sizing: border-box; }
  html, body {
    width: 1200px; height: 1200px; overflow: hidden;
    background: var(--backdrop);
  }
  .letterhead {
    position: absolute; left: 234px; top: 83px;
    width: 731px; height: 1034px;
    background: var(--paper);
    box-shadow: 0 4px 14px rgba(0,0,0,0.18);
    font-family: "Carlito", "Calibri", sans-serif;
    color: var(--ink);
  }
  .brand-name {
    position: absolute; left: 52px; top: 150px;
    font-family: "Montserrat", sans-serif; font-weight: 800;
    font-size: 21px; letter-spacing: 0.2px;
    color: var(--brand-purple);
    transform: translateY(-100%);
    white-space: nowrap;
  }
  .sender-name {
    position: absolute; right: 55px; top: 108px;
    font-family: "Montserrat", sans-serif; font-weight: 700;
    font-size: 17px; color: var(--brand-purple);
  }
  .recipient {
    position: absolute; left: 55px; top: 214px;
    font-size: 13.7px; line-height: 17.7px;
    font-style: normal;
  }
  .salutation {
    position: absolute; left: 55px; top: 351px;
    font-size: 13.7px;
  }
  .letter-body {
    position: absolute; left: 55px; top: 388px; width: 620px;
    font-size: 13.7px; line-height: 22.1px;
    text-align: justify;
  }
  .closing {
    position: absolute; left: 55px; top: 713px;
    font-size: 13.7px;
  }
  .signature {
    position: absolute; left: 52px; top: 733px;
    width: 242px; height: 80px;
  }
  .office-address {
    position: absolute; left: 50px; top: 920px;
    font-family: "Montserrat", sans-serif; font-weight: 500;
    font-size: 11.6px; line-height: 15.4px;
    color: var(--ink-dark); font-style: normal;
  }
  .contact-list {
    position: absolute; right: 53px; top: 890px;
    list-style: none;
    font-family: "Montserrat", sans-serif; font-size: 10.6px;
    line-height: 15.4px; color: var(--ink-dark);
    text-align: right;
  }
  .contact-list li { display: flex; justify-content: flex-end; align-items: center; gap: 6px; }
  .contact-list svg { width: 9px; height: 9px; fill: var(--brand-purple); }
  .footer-rule {
    position: absolute; left: 50px; top: 977px;
    width: 627px; height: 2px; background: var(--brand-purple);
  }
  .web-tab {
    position: absolute; left: 520px; top: 977px;
    width: 157px; height: 16px;
    background: var(--brand-purple);
    clip-path: polygon(0 0, 100% 0, 100% 100%, 10% 100%);
    font-family: "Montserrat", sans-serif; font-size: 11px; font-weight: 500;
    color: #fff; line-height: 16px; text-align: right; padding-right: 14px;
  }
</style>
</head>
<body>
  <main class="letterhead">
    <header>
      <div class="brand-name">Meridian Realty Group, LLC</div>
      <div class="sender-name">DANIEL REYES</div>
    </header>

    <address class="recipient">
      Mr. Alan Hart<br>
      President<br>
      Northfield Accountants<br>
      111 Street Name,<br>
      City State, 12345
    </address>

    <p class="salutation">Dear :</p>

    <div class="letter-body">
      <p>Lorem ipsum dolor sit amet, consectetur adipiscing elit. Aenean ut ipsum eget massa hendrerit vestibulum vel in velit. Donec pretium neque velit.</p>
      <p>Aliquam porta lectus nec mauris ornare venenatis. Vivamus non est turpis, et cursus sem. Mauris vehicula erat in diam auctor at bibendum nisl lacinia.</p>
      <p>Morbi imperdiet neque vehicula nunc convallis gravida. Vestibulum iaculis pretium placerat. Integer consequat, est sit amet facilisis eleifend, nibh nibh varius orci, eget dapibus arcu dui non purus. Pellentesque in magna mauris. Duis enim sapien, dictum vitae condimentum a, pulvinar vel lacus. Mauris et molestie nibh. Vestibulum vitae nulla at metus elementum porta sit amet interdum elit. Nulla sollicitudin neque eu nulla volutpat congue.</p>
      <p>Etiam pellentesque, velit id dapibus fermentum, turpis sapien ornare dui, ac tincidunt ligula odio congue purus. Nunc sed ante dui, in porta lectus. Cras nec sem lorem. In hac habitasse platea dictumst. Maecenas id diam quis dui porta tristique. Sed id egestas felis. Donec ullamcorper mattis posuere. Phasellus fermentum eleifend tortor vel dapibus. Vestibulum ante ipsum.</p>
    </div>

    <p class="closing">Sincerely,</p>
    <svg class="signature" role="img" aria-label="Handwritten signature of Daniel Reyes" viewBox="0 0 242 80">
      <rect width="242" height="80" rx="6" fill="var(--signature-tone)"/>
    </svg>

    <footer>
      <address class="office-address">
        2750 Harbor View Ave,<br>
        Suite 210 Brookside NY 10520
      </address>
      <ul class="contact-list">
        <li>555.210.1000 <svg viewBox="0 0 10 10"><path d="M2.5 0h5a1 1 0 0 1 1 1v8a1 1 0 0 1-1 1h-5a1 1 0 0 1-1-1V1a1 1 0 0 1 1-1zm0.3 1v7.2h4.4V1z"/></svg></li>
        <li>555.340.1400 <svg viewBox="0 0 10 10"><path d="M2 0.5l1.6 2.2-1 1a6 6 0 0 0 3.7 3.7l1-1L9.5 8 8.4 9.5C4 9.5 0.5 6 0.5 1.6z"/></svg></li>
        <li>555.480.8000 <svg viewBox="0 0 10 10"><path d="M2.5 0h5v2.5h-5zM1 3h8a1 1 0 0 1 1 1v3.5H8V6H2v1.5H0V4a1 1 0 0 1 1-1zm1.5 3.5h5V10h-5z"/></svg></li>
        <li>daniel@meridianrealty.com <svg viewBox="0 0 10 10"><path d="M0 2h10v6.5H0zm0.8 0.8L5 5.6l4.2-2.8z" fill-rule="evenodd"/></svg></li>
      </ul>
      <div class="footer-rule"></div>
      <div class="web-tab">www.meridianrealty.com</div>
    </footer>
  </main>
</body>
</html>
```